Business Card Design

New Homes
Renovations/Additions
Building Maintenance
Design
Council Approvals
Estimates
Project and Construction Management

The back of the card should only contain my logo which is attached and under the logo have written velora & velora constructions.

Industry/Entity Type

Business

Contact Information for Business Card

Company Name: Velora & Velora Constructions Pty Ltd
BLD 641372
ABN: 52 907 314 286
Position: Director
Name: Tavo Rilkenbar
Tel: m. 0418276354
f. (08)83926157
veloranvelora@mailnest.example

```html
<!DOCTYPE html>
<html lang="en">
<head>
<meta charset="utf-8">
<title>Velora &amp; Velora Constructions — Business Card</title>
<link rel="stylesheet" href="https://fonts.googleapis.com/css2?family=Libre+Baskerville&family=Arimo:wght@400&display=swap">
<style>
  :root {
    --backdrop: #d9d9d9;
    --card-black: #0c0c0c;
    --card-white: #ffffff;
    --ink-white: #f2f2f2;
    --ink-dark: #2a2a2a;
    --ink-grey: #9a9a9a;
    --rule: #c9c9c9;
  }
  * { margin: 0; padding: 0; box-sizing: border-box; }
  html, body { width: 1200px; height: 873px; overflow: hidden; }
  body {
    background: var(--backdrop);
    display: flex;
    align-items: center;
    justify-content: center;
    gap: 50px;
  }
  .card {
    width: 530px;
    height: 303px;
    position: relative;
    box-shadow: 0 2px 6px rgba(0,0,0,0.18);
  }
  .card--front {
    background: var(--card-black);
    display: flex;
    flex-direction: column;
    align-items: center;
    justify-content: center;
    gap: 26px;
  }
  .brand-mark {
    font-family: "Libre Baskerville", serif;
    color: var(--ink-white);
    font-size: 30px;
    letter-spacing: 1px;
  }
  .brand-name {
    font-family: "Libre Baskerville", serif;
    color: var(--ink-white);
    font-size: 19px;
    letter-spacing: 0.5px;
  }
  .card--back {
    background: var(--card-white);
    font-family: "Arimo", sans-serif;
  }
  .holder-name {
    position: absolute;
    left: 46px;
    top: 48px;
    font-size: 19px;
    letter-spacing: 1px;
    color: var(--ink-dark);
    text-transform: uppercase;
  }
  .holder-role {
    position: absolute;
    left: 150px;
    top: 84px;
    font-size: 11px;
    color: var(--ink-grey);
  }
  .divider {
    position: absolute;
    left: 46px;
    top: 118px;
    width: 240px;
    height: 130px;
  }
  .details {
    position: absolute;
    left: 254px;
    top: 128px;
    list-style: none;
    font-size: 12.5px;
    line-height: 21px;
    color: var(--ink-dark);
  }
</style>
</head>
<body>
  <section class="card card--front" aria-label="Card front">
    <div class="brand-mark">Velora &amp; Velora</div>
    <div class="brand-name">Velora &amp; Velora Constructions</div>
  </section>

  <section class="card card--back" aria-label="Card back">
    <h1 class="holder-name">Tavo Rilkenbar</h1>
    <p class="holder-role">Director</p>
    <svg class="divider" viewBox="0 0 240 130" aria-hidden="true">
      <line x1="0" y1="0.5" x2="200" y2="0.5" stroke="var(--rule)" stroke-width="1"/>
      <line x1="195.5" y1="0" x2="195.5" y2="122" stroke="var(--rule)" stroke-width="1"/>
    </svg>
    <ul class="details">
      <li>BLD 641372</li>
      <li>ABN: 52 907 314 286</li>
      <li>Tel: 0418276354</li>
      <li>Fax: (08)83926157</li>
      <li>veloranvelora@mailnest.example</li>
    </ul>
  </section>
</body>
</html>
```